Velbrook App Homepage Design making customers feel in control of their spend

Hi,
We need a App Homepage design with a UI similar to the attached mock up on an Quillo 4. The app is intended to put customers in control of their usage and spend on their fixed phone, broadband, mobile, gas and electricity.

Please fee free to propose improvements to the background images, icons, colours, etc.

Any questions please let me know.

Thanks
Tomasz

Target Market(s)

Consumer customers

Industry/Entity Type

Internet

Font styles to use
Sans Serif

Colors
3276b5
0255a3
85acd3
cfdeed
ffffff

Requirements
Must have
• Content in line with the guidelines in the attached mock up

```html
<!DOCTYPE html>
<html lang="en">
<head>
<meta charset="utf-8">
<title>Velbrook – Home</title>
<link rel="stylesheet" href="https://fonts.googleapis.com/css2?family=Raleway:wght@400;500;600&display=swap">
<style>
  :root {
    --screen-top: #1d4f7e;
    --screen-mid: #13304f;
    --screen-bottom: #0b1a2c;
    --brand-blue: #3276b5;
    --brand-light: #85acd3;
    --brand-pale: #cfdeed;
    --white: #ffffff;
    --muted: #8fa6bf;
    --track: #0a121d;
    --bar-power: #e0197d;
    --bar-gas: #e8521f;
    --bar-broadband: #5aa0e6;
    --bar-mobile: #9cc31f;
    --bar-landline: #0f4fa8;
    --avatar: #c9a27e;
  }
  * { margin: 0; padding: 0; box-sizing: border-box; }
  html, body { width: 831px; height: 1200px; overflow: hidden; }
  body {
    font-family: "Raleway", sans-serif;
    color: var(--white);
    background: linear-gradient(180deg, var(--screen-top) 0%, var(--screen-mid) 45%, var(--screen-bottom) 100%);
    position: relative;
  }
  .app-header { position: absolute; top: 70px; left: 0; right: 0; height: 120px; }
  .menu-button { position: absolute; left: 48px; top: 48px; }
  .brand {
    position: absolute; left: 110px; top: 34px;
    display: flex; align-items: center; gap: 18px;
  }
  .brand-dot { width: 56px; height: 56px; border-radius: 50%; background: var(--brand-blue); }
  .brand-name { font-size: 46px; font-weight: 500; color: var(--brand-light); }

  .greeting { position: absolute; top: 285px; left: 250px; display: flex; align-items: center; gap: 26px; }
  .avatar {
    width: 88px; height: 88px; border-radius: 50%;
    background: radial-gradient(circle at 50% 40%, #e4c6a6, var(--avatar));
    border: 4px solid var(--white);
  }
  .greeting-title { font-size: 36px; font-weight: 600; }
  .greeting-sub { font-size: 20px; color: var(--muted); margin-top: 6px; }

  .charges-summary {
    position: absolute; top: 455px; left: 200px; right: 110px;
    display: flex; justify-content: space-between; align-items: baseline;
  }
  .charges-label { font-size: 26px; font-weight: 500; }
  .charges-total { font-size: 40px; font-weight: 400; color: var(--muted); }
  .divider { position: absolute; top: 522px; left: 110px; right: 110px; height: 2px; background: rgba(207,222,237,.25); }

  .usage-list { position: absolute; top: 565px; left: 100px; right: 110px; list-style: none; }
  .usage-row { display: flex; align-items: center; height: 100px; }
  .usage-icon { width: 70px; display: flex; justify-content: center; }
  .usage-track { flex: 1; height: 40px; margin-left: 40px; background: var(--track); }
  .usage-fill { height: 100%; }
  .fill-power { width: 38%; background: var(--bar-power); }
  .fill-gas { width: 78%; background: var(--bar-gas); }
  .fill-broadband { width: 24%; background: var(--bar-broadband); }
  .fill-mobile { width: 13%; background: var(--bar-mobile); }
  .fill-landline { width: 19%; background: var(--bar-landline); }

  .latest-bill { position: absolute; top: 1040px; left: 110px; right: 110px; }
  .bill-line { display: flex; align-items: baseline; gap: 26px; }
  .bill-label { font-size: 40px; font-weight: 400; color: var(--brand-pale); }
  .bill-amount { font-size: 40px; font-weight: 500; }
  .bill-meta { display: flex; justify-content: space-between; margin-top: 14px; font-size: 20px; color: var(--muted); }
</style>
</head>
<body>
  <header class="app-header">
    <svg class="menu-button" width="34" height="26" viewBox="0 0 34 26" aria-label="Menu">
      <rect y="0" width="34" height="3" fill="#ffffff"/>
      <rect y="11" width="34" height="3" fill="#ffffff"/>
      <rect y="22" width="34" height="3" fill="#ffffff"/>
    </svg>
    <div class="brand">
      <span class="brand-dot"></span>
      <span class="brand-name">Velbrook</span>
    </div>
  </header>

  <section class="greeting">
    <div class="avatar" role="img" aria-label="Profile photo of the account holder"></div>
    <div>
      <p class="greeting-title">Good morning Sophie</p>
      <p class="greeting-sub">Welcome to Velbrook</p>
    </div>
  </section>

  <section class="charges-summary">
    <span class="charges-label">Your Current Charges</span>
    <span class="charges-total">£63.99</span>
  </section>
  <div class="divider"></div>

  <ul class="usage-list">
    <li class="usage-row">
      <span class="usage-icon">
        <svg width="34" height="46" viewBox="0 0 34 46" aria-label="Electricity"><path d="M17 3a13 13 0 0 0-8 23c2 2 3 4 3 7h10c0-3 1-5 3-7A13 13 0 0 0 17 3z" fill="none" stroke="#fff" stroke-width="3"/><path d="M12 38h10M13 43h8" stroke="#fff" stroke-width="3"/></svg>
      </span>
      <span class="usage-track"><span class="usage-fill fill-power" style="display:block"></span></span>
    </li>
    <li class="usage-row">
      <span class="usage-icon">
        <svg width="34" height="44" viewBox="0 0 34 44" aria-label="Gas"><path d="M17 3c2 9 13 14 13 26a13 13 0 0 1-26 0c0-7 4-10 6-14 1 4 3 6 5 6 0-6-1-12 2-18z" fill="none" stroke="#fff" stroke-width="3" stroke-linejoin="round"/></svg>
      </span>
      <span class="usage-track"><span class="usage-fill fill-gas" style="display:block"></span></span>
    </li>
    <li class="usage-row">
      <span class="usage-icon">
        <svg width="44" height="34" viewBox="0 0 44 34" aria-label="Broadband"><path d="M3 12a27 27 0 0 1 38 0M9 19a18 18 0 0 1 26 0M15 26a9 9 0 0 1 14 0" fill="none" stroke="#fff" stroke-width="3" stroke-linecap="round"/><circle cx="22" cy="31" r="2.5" fill="#fff"/></svg>
      </span>
      <span class="usage-track"><span class="usage-fill fill-broadband" style="display:block"></span></span>
    </li>
    <li class="usage-row">
      <span class="usage-icon">
        <svg width="28" height="46" viewBox="0 0 28 46" aria-label="Mobile"><rect x="2" y="2" width="24" height="42" rx="4" fill="none" stroke="#fff" stroke-width="3"/><path d="M10 37h8" stroke="#fff" stroke-width="3"/></svg>
      </span>
      <span class="usage-track"><span class="usage-fill fill-mobile" style="display:block"></span></span>
    </li>
    <li class="usage-row">
      <span class="usage-icon">
        <svg width="40" height="40" viewBox="0 0 40 40" aria-label="Home phone"><path d="M9 3l7 8-4 5c3 6 7 10 12 12l5-4 8 7-5 6C18 36 4 22 3 9z" fill="none" stroke="#fff" stroke-width="3" stroke-linejoin="round"/></svg>
      </span>
      <span class="usage-track"><span class="usage-fill fill-landline" style="display:block"></span></span>
    </li>
  </ul>

  <section class="latest-bill">
    <div class="bill-line">
      <span class="bill-label">Latest bill</span>
      <span class="bill-amount">£123.99</span>
    </div>
    <div class="bill-meta">
      <span>9 Dec 2016</span>
      <span>Next bill due in 14 days</span>
    </div>
  </section>
</body>
</html>
```